Bref créative
Retro design logo for building Materials company
R.K. Morrow Company
Professional
Peter K. Morrow IV
LEED AP BD+C
342 Ferngate Lane, Suite D
Larkfield, OK 72814
pmorrow@buildwiseterra.com
This is my logo AI file.

```html
<!DOCTYPE html>
<html lang="en">
<head>
<meta charset="utf-8">
<title>R.K. Morrow Company – Business Card</title>
<link rel="stylesheet" href="https://fonts.googleapis.com/css2?family=Josefin+Sans:wght@300;400;600&display=swap">
<style>
  :root {
    --backdrop: #e9e6e1;
    --card-white: #ffffff;
    --charcoal: #3a3a3b;
    --ink: #3d3d3e;
    --reverse: #ffffff;
  }
  * { margin: 0; padding: 0; box-sizing: border-box; }
  html, body {
    width: 1200px;
    height: 914px;
    overflow: hidden;
    background: var(--backdrop);
    font-family: "Josefin Sans", sans-serif;
  }
  .business-card {
    position: absolute;
    left: 100px;
    top: 171px;
    width: 1000px;
    height: 571px;
    background: var(--card-white);
    box-shadow: 0 6px 24px rgba(0, 0, 0, 0.18);
    overflow: hidden;
  }
  .card-shapes {
    position: absolute;
    inset: 0;
  }
  .holder {
    position: absolute;
    left: 56px;
    top: 58px;
    color: var(--ink);
    text-transform: uppercase;
    letter-spacing: 3px;
  }
  .holder-name {
    font-size: 21px;
    font-weight: 400;
  }
  .holder-credential {
    font-size: 18px;
    font-weight: 300;
    margin-top: 6px;
  }
  .contact-list {
    position: absolute;
    left: 56px;
    top: 352px;
    list-style: none;
    color: var(--ink);
    text-transform: uppercase;
    font-size: 13px;
    font-weight: 400;
    letter-spacing: 1px;
  }
  .contact-item {
    display: flex;
    align-items: center;
    gap: 10px;
    height: 24px;
    white-space: nowrap;
  }
  .contact-item.is-continued { padding-left: 26px; }
  .contact-icon {
    width: 16px;
    height: 16px;
    flex: none;
  }
  .brand {
    position: absolute;
    left: 470px;
    top: 200px;
    width: 470px;
    text-align: center;
    color: var(--reverse);
  }
  .brand-ring {
    display: block;
    margin: 0 auto 26px;
    width: 88px;
    height: 88px;
  }
  .brand-name {
    font-size: 40px;
    font-weight: 400;
    letter-spacing: 3px;
    white-space: nowrap;
  }
</style>
</head>
<body>
  <article class="business-card" aria-label="R.K. Morrow Company business card">
    <svg class="card-shapes" viewBox="0 0 1000 571" aria-hidden="true">
      <path d="M535 0 Q375 250 395 571" fill="none" stroke="var(--charcoal)" stroke-width="8"/>
      <path d="M562 0 Q402 250 422 571 L1000 571 L1000 0 Z" fill="var(--charcoal)"/>
    </svg>

    <header class="holder">
      <p class="holder-name">Peter K. Morrow IV</p>
      <p class="holder-credential">LEED AP BD+C</p>
    </header>

    <ul class="contact-list">
      <li class="contact-item">
        <svg class="contact-icon" viewBox="0 0 16 16" aria-hidden="true">
          <circle cx="8" cy="8" r="8" fill="var(--ink)"/>
          <path d="M8 3.5a3 3 0 0 0-3 3c0 2.2 3 5.8 3 5.8s3-3.6 3-5.8a3 3 0 0 0-3-3z" fill="#fff"/>
          <circle cx="8" cy="6.5" r="1.1" fill="var(--ink)"/>
        </svg>
        <span>342 Ferngate Lane, Suite D</span>
      </li>
      <li class="contact-item is-continued"><span>Larkfield, OK 72814</span></li>
      <li class="contact-item">
        <svg class="contact-icon" viewBox="0 0 16 16" aria-hidden="true">
          <circle cx="8" cy="8" r="8" fill="var(--ink)"/>
          <path d="M5.2 4.2l1.4-.4 1 2.1-.9.7a5 5 0 0 0 2.7 2.7l.7-.9 2.1 1-.4 1.4c-3.3.2-6.8-3.3-6.6-6.6z" fill="#fff"/>
        </svg>
        <span>600-555-0148</span>
      </li>
      <li class="contact-item">
        <svg class="contact-icon" viewBox="0 0 16 16" aria-hidden="true">
          <circle cx="8" cy="8" r="8" fill="var(--ink)"/>
          <rect x="4" y="5.2" width="8" height="5.6" fill="#fff"/>
          <path d="M4 5.2l4 3 4-3" fill="none" stroke="var(--ink)" stroke-width="0.9"/>
        </svg>
        <span>pmorrow@buildwiseterra.com</span>
      </li>
    </ul>

    <div class="brand">
      <svg class="brand-ring" viewBox="0 0 88 88" aria-hidden="true">
        <circle cx="44" cy="44" r="41" fill="none" stroke="var(--reverse)" stroke-width="4"/>
      </svg>
      <p class="brand-name">R.K. MORROW CO.</p>
    </div>
  </article>
</body>
</html>
```